Thermostat Screen Design

We need a screen layout design for a new thermostat we're currently developing. If you're not familiar with thermostats, you can see some examples here - http://heating-dials-compared.bestlistguide.example/

We're after the main page design, with icons, colours etc. It needs to be clean, modern and minimalistic. Attached is all components required on the screen. The screen size is 5 inch (diagnol).

The arrows on the screen showcase what happens when you press a button. For example, when you press MODE once you get OFF, press it twice, HEAT, press it 3 times, COOL, etc. This is just for your reference.

You have complete creative license on how you choose to layout the screen, position the components etc, but we require:

- it must be on a 5 inch screen diagnol
- modern, clean and minimalistic
- includes icons and colours
- Intuitive

Let me know if any questions.

```html
<!DOCTYPE html>
<html lang="en">
<head>
<meta charset="utf-8">
<title>Thermostat Main Screen</title>
<link href="https://fonts.googleapis.com/css2?family=Titillium+Web:wght@200;300;400&display=swap" rel="stylesheet">
<style>
  :root{
    --bg:#06426a;
    --sidebar:#0a4b74;
    --divider:#053a5c;
    --border:#2b6a92;
    --row:#1e5a80;
    --row-line:#3a7398;
    --text:#ffffff;
    --muted:#7fa8c4;
    --icon:#6f9dbd;
    --accent:#0b5a90;
    --button-light:#f4f8fb;
  }
  *{box-sizing:border-box;margin:0;padding:0}
  html,body{width:1200px;height:680px;overflow:hidden;background:var(--bg)}
  body{font-family:"Titillium Web",sans-serif;color:var(--text);position:relative}

  .sidebar{position:absolute;left:0;top:0;width:170px;height:680px;background:var(--sidebar);border-right:2px solid var(--divider)}
  .nav-item{position:absolute;left:0;width:168px;height:170px;display:flex;flex-direction:column;align-items:center;justify-content:center;gap:10px;color:var(--muted);font-size:23px;font-weight:400}
  .nav-item + .nav-item{border-top:3px solid var(--divider)}
  .nav-item svg{display:block}
  .nav-mode{top:0;height:168px}
  .nav-fan{top:168px;height:171px}
  .nav-settings{top:339px;height:171px}
  .nav-zones{top:510px}

  .chip{position:absolute;border:2px solid var(--border);border-radius:6px;display:flex;align-items:center;justify-content:center;gap:10px;font-size:22px;font-weight:400;color:var(--text)}
  .chip-outdoor{left:226px;top:15px;width:242px;height:51px}
  .chip-humidity{left:479px;top:15px;width:210px;height:51px}
  .chip-sleep{left:745px;top:15px;width:178px;height:51px}
  .chip-zone{left:955px;top:15px;width:180px;height:51px}
  .chip-date{left:746px;top:82px;width:387px;height:46px}

  .temp-panel{position:absolute;left:222px;top:84px;width:469px;height:475px;border:2px solid var(--border);border-radius:6px;overflow:hidden}
  .temp-label{position:absolute;top:30px;width:100%;text-align:center;font-size:30px;font-weight:300}
  .temp-value{position:absolute;left:0;top:58px;width:100%;text-align:center;font-size:305px;line-height:300px;font-weight:200;letter-spacing:-8px}
  .temp-degree{position:absolute;left:396px;top:90px;font-size:42px;font-weight:200}

  .setpoint{position:absolute;left:0;width:384px;height:64px;background:var(--row);display:flex;align-items:center;justify-content:flex-end;padding-right:32px;gap:10px;font-size:26px;font-weight:300;color:var(--muted)}
  .setpoint .value{color:var(--text);font-weight:400;width:60px;text-align:left;margin-left:18px}
  .setpoint-cool{top:343px}
  .setpoint-heat{top:411px;height:64px}
  .step-btn{position:absolute;left:384px;width:85px;background:var(--button-light);display:flex;align-items:center;justify-content:center}
  .step-up{top:343px;height:66px}
  .step-down{top:411px;height:64px}

  .clock{position:absolute;left:746px;top:166px;width:390px;height:390px;border:2px solid var(--border);border-radius:50%}
  .clock-time{position:absolute;top:100px;width:100%;text-align:center;font-size:104px;line-height:120px;font-weight:200;letter-spacing:2px}
  .clock-period{position:absolute;top:222px;width:100%;text-align:center;font-size:42px;font-weight:300;color:var(--muted)}

  .action{position:absolute;top:596px;height:68px;border:2px solid var(--border);border-radius:6px;display:flex;align-items:center;justify-content:center;gap:18px;font-size:24px;font-weight:400}
  .action-mode{left:226px;width:224px}
  .action-fan{left:466px;width:224px}
  .action-cool{left:709px;width:223px}
  .action-zone{left:949px;width:225px}
</style>
</head>
<body>

<nav class="sidebar">
  <div class="nav-item nav-mode">
    <svg width="60" height="58" viewBox="0 0 60 58" aria-hidden="true">
      <g stroke="var(--icon)" stroke-width="4" stroke-linecap="round" fill="none">
        <line x1="22" y1="4" x2="22" y2="40"/><line x1="6" y1="13" x2="38" y2="31"/><line x1="6" y1="31" x2="38" y2="13"/>
        <polyline points="16,7 22,12 28,7"/><polyline points="16,37 22,32 28,37"/>
      </g>
      <path d="M44 24c6 8 12 14 12 22a11 11 0 0 1-22 0c0-6 4-9 5-14 2 4 4 5 5 8 2-5 1-11 0-16z" fill="var(--icon)"/>
    </svg>
    <span>Mode</span>
  </div>
  <div class="nav-item nav-fan">
    <svg width="70" height="70" viewBox="0 0 70 70" aria-hidden="true">
      <g fill="var(--icon)">
        <path d="M35 30C26 22 20 12 28 5c9-6 18 3 14 15-2 5-4 8-7 10z"/>
        <path d="M39 38c11-3 22-1 22 9-1 11-13 12-20 3-3-4-3-8-2-12z"/>
        <path d="M30 38c-2 11-9 20-18 15-9-6-4-17 8-19 4-1 7 1 10 4z"/>
        <circle cx="35" cy="35" r="6"/>
      </g>
    </svg>
    <span>Fan</span>
  </div>
  <div class="nav-item nav-settings">
    <svg width="60" height="62" viewBox="0 0 60 62" aria-hidden="true">
      <g stroke="var(--icon)" stroke-width="4" stroke-linecap="round">
        <line x1="10" y1="4" x2="10" y2="58"/><line x1="30" y1="4" x2="30" y2="58"/><line x1="50" y1="4" x2="50" y2="58"/>
      </g>
      <g fill="var(--icon)">
        <rect x="3" y="14" width="14" height="10" rx="2"/><rect x="23" y="36" width="14" height="10" rx="2"/><rect x="43" y="22" width="14" height="10" rx="2"/>
      </g>
    </svg>
    <span>Settings</span>
  </div>
  <div class="nav-item nav-zones">
    <svg width="70" height="50" viewBox="0 0 70 50" aria-hidden="true">
      <g stroke="var(--icon)" stroke-width="4" stroke-linecap="round" fill="none">
        <path d="M14 6c-10 12-10 26 0 38"/><path d="M56 6c10 12 10 26 0 38"/>
        <path d="M24 16c-5 6-5 12 0 18"/><path d="M46 16c5 6 5 12 0 18"/>
      </g>
    </svg>
    <span>Zones</span>
  </div>
</nav>

<div class="chip chip-outdoor">Outdoor Temp: 28º</div>
<div class="chip chip-humidity">Indoor RH: 20%</div>
<div class="chip chip-sleep">SLEEP</div>
<div class="chip chip-zone">ZONE 1</div>
<div class="chip chip-date">
  <svg width="20" height="20" viewBox="0 0 20 20" aria-hidden="true">
    <rect x="1" y="3" width="18" height="16" rx="2" fill="var(--muted)"/>
    <g fill="var(--bg)"><rect x="4" y="8" width="3" height="3"/><rect x="9" y="8" width="3" height="3"/><rect x="14" y="8" width="3" height="3"/><rect x="4" y="13" width="3" height="3"/><rect x="9" y="13" width="3" height="3"/></g>
  </svg>
  <span>07-04-2014</span>
</div>

<section class="temp-panel">
  <div class="temp-label">Room Temp</div>
  <div class="temp-value">26</div>
  <div class="temp-degree">o</div>

  <div class="setpoint setpoint-cool">
    <svg width="30" height="30" viewBox="0 0 30 30" aria-hidden="true">
      <g stroke="var(--muted)" stroke-width="2.5" stroke-linecap="round" fill="none">
        <line x1="15" y1="2" x2="15" y2="28"/><line x1="4" y1="8" x2="26" y2="22"/><line x1="4" y1="22" x2="26" y2="8"/>
        <polyline points="11,4 15,8 19,4"/><polyline points="11,26 15,22 19,26"/>
      </g>
    </svg>
    <span>Cool Setpoint:</span><span class="value">55</span>
  </div>
  <div class="setpoint setpoint-heat">
    <svg width="24" height="30" viewBox="0 0 24 30" aria-hidden="true">
      <path d="M12 2c6 8 10 13 10 19a10 10 0 0 1-20 0c0-5 3-8 4-12 2 3 3 5 4 7 2-5 2-10 2-14z" fill="var(--muted)"/>
    </svg>
    <span>Heat Setpoint:</span><span class="value">68</span>
  </div>
  <div class="step-btn step-up">
    <svg width="34" height="22" viewBox="0 0 34 22" aria-hidden="true"><polyline points="4,18 17,5 30,18" stroke="var(--accent)" stroke-width="6" fill="none"/></svg>
  </div>
  <div class="step-btn step-down">
    <svg width="34" height="22" viewBox="0 0 34 22" aria-hidden="true"><polyline points="4,4 17,17 30,4" stroke="var(--accent)" stroke-width="6" fill="none"/></svg>
  </div>
</section>

<section class="clock">
  <div class="clock-time">09:26</div>
  <div class="clock-period">AM</div>
</section>

<div class="action action-mode">Heat</div>
<div class="action action-fan">
  <svg width="44" height="44" viewBox="0 0 70 70" aria-hidden="true">
    <g fill="none" stroke="var(--muted)" stroke-width="4">
      <path d="M35 30C26 22 20 12 28 5c9-6 18 3 14 15-2 5-4 8-7 10z"/>
      <path d="M39 38c11-3 22-1 22 9-1 11-13 12-20 3-3-4-3-8-2-12z"/>
      <path d="M30 38c-2 11-9 20-18 15-9-6-4-17 8-19 4-1 7 1 10 4z"/>
      <circle cx="35" cy="35" r="6"/>
    </g>
  </svg>
  <span>Auto</span>
</div>
<div class="action action-cool">
  <svg width="46" height="46" viewBox="0 0 30 30" aria-label="Cooling" role="img">
    <g stroke="var(--muted)" stroke-width="2.5" stroke-linecap="round" fill="none">
      <line x1="15" y1="2" x2="15" y2="28"/><line x1="4" y1="8" x2="26" y2="22"/><line x1="4" y1="22" x2="26" y2="8"/>
      <polyline points="11,4 15,8 19,4"/><polyline points="11,26 15,22 19,26"/>
      <polyline points="3,12 7,10 5,6"/><polyline points="27,18 23,20 25,24"/>
      <polyline points="3,18 7,20 5,24"/><polyline points="27,12 23,10 25,6"/>
    </g>
  </svg>
</div>
<div class="action action-zone">Zone 1</div>

</body>
</html>
```